KQW Authorised Dealer needs Business Cards

We need a business card designed for our branch owners. Vellmor Alarms is an Authorised KQW Dealer and does its own independent installations outside of the KQW work we perform so whilst the KQW Authorised Dealer Logo needs to be included, it should not be overwhelming in respect of the overall look of the card. I would like a rounded edge to the cards corners rather than a 90 degree hard edge. We also need to promote the fact that we do First Class Alarm & CCTV Solutions. (Details of card holder to follow)

```html
<!DOCTYPE html>
<html lang="en">
<head>
<meta charset="utf-8">
<title>Vellmor Alarms – Business Card</title>
<link href="https://fonts.googleapis.com/css2?family=Oswald:wght@500;600&family=Play:wght@400;700&display=swap" rel="stylesheet">
<style>
  :root{
    --brand-blue:#1a76bd;
    --ink-grey:#4d4f53;
    --soft-grey:#8a8c90;
    --rule-grey:#dcdde0;
    --card-white:#ffffff;
    --page-bg:#eceae6;
  }
  *{margin:0;padding:0;box-sizing:border-box}
  html,body{width:1200px;height:1018px;overflow:hidden;background:var(--page-bg)}
  .sheet{position:relative;width:1200px;height:1018px}
  .card{
    position:absolute;left:190px;width:820px;height:468px;border-radius:22px;
    box-shadow:0 6px 20px rgba(0,0,0,.12);overflow:hidden
  }
  .card--front{top:30px;background:var(--card-white)}
  .card--back{top:520px;background:var(--brand-blue)}
  .card__divider{position:absolute;left:652px;top:0;width:1px;height:100%;background:var(--rule-grey)}

  .brand{position:absolute;left:52px;top:62px;display:flex;align-items:center;gap:18px}
  .brand__mark{width:46px;height:46px;background:var(--brand-blue)}
  .brand__name{
    font-family:"Oswald",sans-serif;font-weight:600;font-size:56px;line-height:1;
    letter-spacing:1px;color:var(--brand-blue);text-transform:uppercase;white-space:nowrap
  }
  .brand__rule{position:absolute;left:52px;top:150px;width:560px;height:4px;background:var(--brand-blue)}

  .holder{position:absolute;left:52px;top:200px;padding-left:18px;border-left:4px solid var(--brand-blue)}
  .holder__name{
    font-family:"Oswald",sans-serif;font-weight:500;font-size:38px;line-height:1.05;
    color:var(--brand-blue);text-transform:uppercase;letter-spacing:1px
  }
  .holder__role{
    font-family:"Play",sans-serif;font-size:15px;letter-spacing:2px;color:var(--ink-grey);
    text-transform:uppercase;margin-top:6px
  }

  .contacts{
    position:absolute;left:52px;top:318px;display:grid;grid-template-columns:230px 320px;
    row-gap:14px;font-family:"Play",sans-serif;font-size:16px;color:var(--ink-grey)
  }
  .contacts__item{display:flex;align-items:center;gap:10px;white-space:nowrap}
  .contacts__item--wide{grid-column:1 / span 2}
  .contacts__icon{width:16px;height:16px;flex:none;fill:var(--ink-grey)}

  .dealer{
    position:absolute;left:653px;top:0;width:167px;height:100%;
    display:flex;flex-direction:column;align-items:center;justify-content:center;gap:10px;text-align:center
  }
  .dealer__dot{width:40px;height:40px;border-radius:50%;background:var(--soft-grey)}
  .dealer__name{
    font-family:"Oswald",sans-serif;font-weight:600;font-size:34px;line-height:1;
    color:var(--ink-grey);letter-spacing:2px
  }
  .dealer__label{
    font-family:"Play",sans-serif;font-size:12px;line-height:1.4;letter-spacing:1.5px;
    color:var(--soft-grey);text-transform:uppercase
  }

  .back{
    position:absolute;inset:0;display:flex;flex-direction:column;align-items:center;justify-content:center;
    gap:22px;color:var(--card-white);text-align:center
  }
  .back__name{
    font-family:"Oswald",sans-serif;font-weight:600;font-size:60px;line-height:1;
    letter-spacing:2px;text-transform:uppercase
  }
  .back__rule{width:120px;height:3px;background:var(--card-white)}
  .back__tagline{
    font-family:"Play",sans-serif;font-size:22px;letter-spacing:3px;text-transform:uppercase
  }
</style>
</head>
<body>
<main class="sheet">
  <section class="card card--front" aria-label="Business card front">
    <div class="brand">
      <span class="brand__mark"></span>
      <span class="brand__name">Vellmor Alarms</span>
    </div>
    <div class="brand__rule"></div>

    <div class="holder">
      <p class="holder__name">Daniel Reyes</p>
      <p class="holder__role">General Manager</p>
    </div>

    <div class="contacts">
      <p class="contacts__item">
        <svg class="contacts__icon" viewBox="0 0 16 16"><path d="M3.5 1.5l2.5 0 1 3.5-1.6 1.2a8 8 0 0 0 4.4 4.4L11 9l3.5 1v2.5c0 1-1 2-2 2C6.6 14.5 1.5 9.4 1.5 3.5c0-1 1-2 2-2z"/></svg>
        012 555 0147
      </p>
      <p class="contacts__item">
        <svg class="contacts__icon" viewBox="0 0 16 16"><path d="M1 3h14v10H1z M2.5 4.5v.4L8 8.6l5.5-3.7v-.4z" fill-rule="evenodd"/></svg>
        info@vellmoralarms.com
      </p>
      <p class="contacts__item">
        <svg class="contacts__icon" viewBox="0 0 16 16"><path d="M3 1h10v14H3z M4.5 2.5v9h7v-9z M7 12.5h2v1H7z" fill-rule="evenodd"/></svg>
        012 555 0148
      </p>
      <p class="contacts__item">
        <svg class="contacts__icon" viewBox="0 0 16 16"><path d="M8 1a7 7 0 1 0 0 14A7 7 0 0 0 8 1zm-1 1.6C5.6 4 5 5.8 5 7.3H2.6A5.5 5.5 0 0 1 7 2.6zm2 0a5.5 5.5 0 0 1 4.4 4.7H11C11 5.8 10.4 4 9 2.6zM6.5 7.3C6.5 5.6 7.1 4 8 3c.9 1 1.5 2.6 1.5 4.3zm-3.9 1.4H5c0 1.5.6 3.3 2 4.7a5.5 5.5 0 0 1-4.4-4.7zm3.9 0h3c0 1.7-.6 3.3-1.5 4.3-.9-1-1.5-2.6-1.5-4.3zm4.5 0h2.4A5.5 5.5 0 0 1 9 13.4c1.4-1.4 2-3.2 2-4.7z"/></svg>
        www.vellmoralarms.com
      </p>
      <p class="contacts__item contacts__item--wide">
        <svg class="contacts__icon" viewBox="0 0 16 16"><path d="M8 1a5 5 0 0 0-5 5c0 3.6 5 9 5 9s5-5.4 5-9a5 5 0 0 0-5-5zm0 7a2 2 0 1 1 0-4 2 2 0 0 1 0 4z"/></svg>
        42 Harlow Road, Unit 3, West Ward
      </p>
    </div>

    <div class="card__divider"></div>

    <div class="dealer">
      <span class="dealer__dot"></span>
      <p class="dealer__name">KQW</p>
      <p class="dealer__label">Authorised<br>Dealer</p>
    </div>
  </section>

  <section class="card card--back" aria-label="Business card back">
    <div class="back">
      <p class="back__name">Vellmor Alarms</p>
      <span class="back__rule"></span>
      <p class="back__tagline">First Class Alarm &amp; CCTV Solutions</p>
    </div>
  </section>
</main>
</body>
</html>
```